Screen Tides - Report on digital habits and attitudes

We are a research company and we have written a PowerPoint Report to present the results of a series of surveys conducted in the last three years. The research is about the "Screen Tides": people are facing the opportunities and challanges of their lives transformed by the digital technologies. We have investigated a number of topics through thousands of interviews and we've analyzed the data presented in the PowerPoint document.
We're not quite satisfied with the look and feel of the report: it looks too flat and boring, too "basic" to be presented as a professional work, yet being just that. We'd like you to upgrade the graphics and style of the report up to the level of a professional research product. The document still needs to be fully editable (either text and charts) but you can rearrange all the contents as you please, adding images, changing font and text size, colors and whatever you think is necessary to reach our goal.

Target Market(s)

Media covering digital issues
Marketing executives
Public institutions and policy makers

Industry/Entity Type

Market Research

Requirements
Must have
• The treats of a professional work
Fully editable within PowerPoint (either text and charts)
Nice to have
• Smart images
Original organization of the pages
Colors and graphics coherent with the corvalmeadow.it logo/website look and feel
Should not have
• PPT document over 30 MBytes
Images violating copyright

```html
<!DOCTYPE html>
<html lang="it">
<head>
<meta charset="utf-8">
<title>Screen Tides – Indice</title>
<link rel="stylesheet" href="https://fonts.googleapis.com/css2?family=Carlito:wght@400;700&display=swap">
<style>
  :root {
    --navy: #002060;
    --rule: #d9d9d9;
    --ink: #000000;
    --footer-ink: #1a1a1a;
    --ch-grey: #a5a5a5;
    --ch-blue: #4472c4;
    --ch-orange: #ed7d31;
    --ch-gold: #ffc000;
    --ch-green: #70ad47;
    --ch-sky: #5b9bd5;
    --ch-slate: #44546a;
    --accent-top: #c3c98f;
    --accent-bottom: #9aa55a;
    --brand-dot: #ed7d31;
  }
  * { margin: 0; padding: 0; box-sizing: border-box; }
  html, body { width: 760px; height: 1200px; overflow: hidden; background: #fff; }
  body { position: relative; font-family: "Carlito", "Calibri", sans-serif; }

  .top-band { position: absolute; left: 95px; top: 0; width: 421px; height: 10px; background: var(--navy); }

  .section-label { position: absolute; left: 95px; top: 115px; height: 26px; display: flex; align-items: center; }
  .section-label__marker { width: 8px; height: 26px; background: linear-gradient(to right, var(--accent-top), var(--accent-bottom)); }
  .section-label__text { margin-left: 8px; font-size: 19px; color: var(--ink); line-height: 1; }

  .page-number { position: absolute; left: 650px; top: 126px; font-size: 11px; color: var(--ink); }

  .toc { position: absolute; left: 95px; top: 234px; width: 573px; list-style: none; }
  .toc__item {
    height: 117px; display: flex; align-items: center; justify-content: space-between;
    padding: 0 9px 0 8px; border-top: 1px solid var(--rule);
    font-weight: 700; font-size: 19px;
  }
  .toc__page { color: var(--navy); }
  .toc__item--grey   .toc__title { color: var(--ch-grey); }
  .toc__item--blue   .toc__title { color: var(--ch-blue); }
  .toc__item--orange .toc__title { color: var(--ch-orange); }
  .toc__item--gold   .toc__title { color: var(--ch-gold); }
  .toc__item--green  .toc__title { color: var(--ch-green); }
  .toc__item--sky    .toc__title { color: var(--ch-sky); }
  .toc__item--slate  .toc__title { color: var(--ch-slate); }

  .footer { position: absolute; left: 95px; top: 1121px; display: flex; align-items: center; font-size: 10px; color: var(--footer-ink); }
  .footer__mark { width: 10px; height: 10px; border-radius: 50%; background: var(--brand-dot); margin-right: 10px; }
  .footer__text { white-space: pre; }
</style>
</head>
<body>
  <div class="top-band"></div>

  <div class="section-label">
    <span class="section-label__marker"></span>
    <span class="section-label__text">Indice</span>
  </div>
  <div class="page-number">1</div>

  <ol class="toc">
    <li class="toc__item toc__item--grey"><span class="toc__title">Capitolo 1</span><span class="toc__page">01</span></li>
    <li class="toc__item toc__item--blue"><span class="toc__title">Capitolo 1</span><span class="toc__page">04</span></li>
    <li class="toc__item toc__item--orange"><span class="toc__title">Capitolo 1</span><span class="toc__page">10</span></li>
    <li class="toc__item toc__item--gold"><span class="toc__title">Capitolo 1</span><span class="toc__page">15</span></li>
    <li class="toc__item toc__item--green"><span class="toc__title">Capitolo 1</span><span class="toc__page">20</span></li>
    <li class="toc__item toc__item--sky"><span class="toc__title">Capitolo 1</span><span class="toc__page">24</span></li>
    <li class="toc__item toc__item--slate"><span class="toc__title">Capitolo 1</span><span class="toc__page">28</span></li>
  </ol>

  <footer class="footer">
    <span class="footer__mark" aria-hidden="true"></span>
    <span class="footer__text">|   Screen Tides |   dicembre 2020 |   © Corvalmeadow 2020</span>
  </footer>
</body>
</html>
```